Need a Brochure Design

We need a brochure designed (A4 two sides or A3 foldable which is equal to 2 x A4 = total of four pages )

Brief and Logo attached.

```html
<!DOCTYPE html>
<html lang="en">
<head>
<meta charset="utf-8">
<title>Nest Staging Co – Brochure</title>
<link href="https://fonts.googleapis.com/css2?family=Exo+2:wght@400;500;700&family=Raleway:wght@400;500&family=Oswald:wght@500;700&family=Josefin+Sans:wght@300;400&display=swap" rel="stylesheet">
<style>
:root{
  --stage:#8a8a88;
  --paper:#ffffff;
  --peach:#fde6d2;
  --peach-soft:#fff4ea;
  --orange:#f28a44;
  --ink:#222222;
  --body:#555555;
  --dark:#2e3133;
}
*{margin:0;padding:0;box-sizing:border-box}
html,body{width:1200px;height:856px;overflow:hidden;background:var(--stage)}
.canvas{position:relative;width:1200px;height:856px}
.page{position:absolute;top:119px;width:725px;height:1024px;transform:scale(.6);transform-origin:0 0;overflow:hidden;
  background:radial-gradient(ellipse at 80% 70%,var(--peach) 0%,transparent 55%),radial-gradient(ellipse at 20% 90%,var(--peach) 0%,transparent 50%),linear-gradient(var(--paper),var(--peach-soft));
  font-family:'Raleway',sans-serif;color:var(--body)}
.page--front{left:145px}
.page--back{left:625px;background:radial-gradient(ellipse at 30% 20%,var(--peach) 0%,transparent 60%),radial-gradient(ellipse at 80% 85%,var(--peach) 0%,transparent 45%),linear-gradient(var(--peach-soft),var(--paper))}
.abs{position:absolute}
.photo{position:absolute;background:#fff;padding:4px;box-shadow:0 1px 4px rgba(0,0,0,.18)}
.photo > div{width:100%;height:100%}
.heading{font-family:'Exo 2',sans-serif;color:var(--orange);font-size:18px;text-decoration:underline;text-underline-offset:3px;text-decoration-thickness:1px}
.copy{font-size:11px;line-height:14.6px;text-align:justify}
.copy p+p{margin-top:14px}
.brand-badge{position:absolute;left:508px;top:-18px;width:190px;height:190px;border-radius:50%;background:radial-gradient(circle,#fff 55%,var(--peach) 100%);display:flex;align-items:center;justify-content:center;gap:6px}
.brand-name{font-family:'Exo 2',sans-serif;font-weight:500;font-size:15px;color:var(--ink);letter-spacing:1px}
.dot{width:8px;height:8px;border-radius:50%;background:var(--orange)}
.why{position:absolute;left:361px;top:714px;width:322px}
.why-head{background:var(--orange);color:#fff;font-family:'Exo 2',sans-serif;font-size:17px;padding:3px 12px;height:28px}
.why-list{background:var(--dark);color:#fff;list-style:none;font-size:11px;padding:10px 14px;height:100px}
.why-list li{display:flex;align-items:center;gap:6px;line-height:15.8px}
.tick{flex:none}
.cta{font-family:'Exo 2',sans-serif;color:var(--orange);font-size:14.5px;text-decoration:underline;text-underline-offset:3px;line-height:18px}
.phone{display:flex;align-items:center;gap:4px;font-family:'Exo 2',sans-serif;font-weight:700;color:var(--ink);font-size:26px}
.email{font-size:11.5px;color:var(--ink)}
.voucher-1{font-family:'Josefin Sans',sans-serif;font-weight:300;font-size:38px;color:var(--ink);letter-spacing:1px}
.voucher-2{font-family:'Oswald',sans-serif;font-weight:700;font-size:28px;color:var(--ink);line-height:30px}
.voucher-3{font-family:'Oswald',sans-serif;font-weight:500;font-size:14px;color:var(--ink)}
.headline{position:absolute;left:46px;top:38px;width:640px;font-family:'Exo 2',sans-serif;color:var(--ink);font-size:21px;line-height:22px;text-align:center}
.headline b{font-weight:700}
.plans{position:absolute;left:44px;top:105px;width:638px;height:240px;border:1.5px solid var(--orange)}
.plans-head{height:37px;background:var(--orange);color:#fff;font-family:'Exo 2',sans-serif;font-weight:700;font-size:20px;text-align:center;line-height:37px}
.plans-grid{display:grid;grid-template-columns:1fr 1fr;grid-template-rows:1fr 1fr;height:201px}
.plan{padding:16px 0 0 27px;border-right:1.5px solid var(--orange);border-bottom:1.5px solid var(--orange)}
.plan:nth-child(2n){border-right:none}
.plan:nth-child(n+3){border-bottom:none}
.plan h3{font-family:'Exo 2',sans-serif;font-weight:700;font-size:20px;color:var(--ink);line-height:22px}
.plan .incl{font-family:'Exo 2',sans-serif;font-weight:700;font-size:12.5px;color:var(--ink)}
.plan .price{font-family:'Exo 2',sans-serif;font-size:17px;color:var(--ink);margin-top:2px}
.plan .price b{color:var(--orange)}
.plan .price s{color:#666}
.plan .price span{color:var(--orange)}
.footnote{position:absolute;left:0;top:337px;width:725px;text-align:center;font-size:11.5px;color:var(--ink)}
.footnote span{background:var(--peach-soft);padding:0 3px}
.benefits{position:absolute;left:42px;top:714px;list-style:none;font-size:13.5px;color:#444}
.benefits li{display:flex;align-items:center;gap:8px;line-height:19.5px}
.footer{position:absolute;left:0;top:972px;width:725px;height:52px;background:var(--dark);display:flex;align-items:center;justify-content:space-between;padding:0 28px 0 39px;color:#fff;font-family:'Exo 2',sans-serif;font-size:17px}
.footer b{color:var(--orange)}
.social{display:flex;gap:4px}
.social i{width:18px;height:18px;border-radius:50%;background:var(--orange);display:block}
</style>
</head>
<body>
<div class="canvas">

  <!-- Front side -->
  <section class="page page--front">
    <div class="photo" style="left:16px;top:16px;width:694px;height:338px">
      <div role="img" aria-label="Bright staged living room with grey sofas, cushions, rug and wall art" style="background:linear-gradient(180deg,#e9e9e7 0%,#dcdcd8 55%,#b9b3a8 100%)"></div>
    </div>
    <div class="brand-badge"><span class="dot"></span><span class="brand-name">Nest Staging Co</span></div>
    <div class="photo" style="left:44px;top:302px;width:270px;height:272px">
      <div role="img" aria-label="Group portrait of the styling team in white and black outfits" style="background:linear-gradient(180deg,#d8d8d8 0%,#c9c9c9 60%,#8c6a4e 100%)"></div>
    </div>

    <div class="abs heading" style="left:358px;top:388px">Hey There,</div>
    <div class="abs copy" style="left:358px;top:430px;width:325px">
      <p>I'm Mara, Owner and Creative Director of Nest Staging Co. Please let me introduce you to our amazingly creative property styling team!</p>
      <p>We are a friendly bunch who are passionate about home staging. We've been property staging apartments, town-houses, and standalone homes since 2009. An all-female powerhouse, we combine our experience in art, interior design, retail, and business to offer professional home styling throughout Melbourne.</p>
    </div>

    <div class="abs heading" style="left:43px;top:605px">Because First Impressions Count</div>
    <div class="abs copy" style="left:43px;top:644px;width:273px">
      <p>A gorgeous looking home sells faster and fetches a higher price.</p>
      <p>At NestStagingCo, we help our property clients create a lasting impression with minimal spend. Our property vendors are usually looking for home-staging on a tight budget. They come to us searching for creative transformations to help them sell well. Thoughtfully positioned furniture and on-trend interior décor can make all the difference!</p>
      <p>Our property styling service includes a free consultation, longer rental periods, &amp; installation &amp; removal.</p>
    </div>

    <div class="abs heading" style="left:362px;top:605px">We're Well-Connected</div>
    <div class="abs copy" style="left:362px;top:644px;width:321px">
      <p>We have a steady flow of clients who have not yet secured their Real Estate Agents, so we'd be happy to share the love. We believe in last relationships, and we work with reputable agents across Melbourne.</p>
    </div>

    <div class="why">
      <div class="why-head">Why Choose NestStagingCo?</div>
      <ul class="why-list">
        <li><svg class="tick" width="10" height="10" viewBox="0 0 10 10"><circle cx="5" cy="5" r="5" fill="#f28a44"/><path d="M2.6 5.2l1.6 1.5 3.2-3.3" stroke="#fff" stroke-width="1.3" fill="none"/></svg>Experienced, enthusiastic property stylists</li>
        <li><svg class="tick" width="10" height="10" viewBox="0 0 10 10"><circle cx="5" cy="5" r="5" fill="#f28a44"/><path d="M2.6 5.2l1.6 1.5 3.2-3.3" stroke="#fff" stroke-width="1.3" fill="none"/></svg>Work with low client budgets</li>
        <li><svg class="tick" width="10" height="10" viewBox="0 0 10 10"><circle cx="5" cy="5" r="5" fill="#f28a44"/><path d="M2.6 5.2l1.6 1.5 3.2-3.3" stroke="#fff" stroke-width="1.3" fill="none"/></svg>Fast turnaround to a tight deadline</li>
        <li><svg class="tick" width="10" height="10" viewBox="0 0 10 10"><circle cx="5" cy="5" r="5" fill="#f28a44"/><path d="M2.6 5.2l1.6 1.5 3.2-3.3" stroke="#fff" stroke-width="1.3" fill="none"/></svg>Flexible rental terms (4/6/8 weeks)</li>
        <li><svg class="tick" width="10" height="10" viewBox="0 0 10 10"><circle cx="5" cy="5" r="5" fill="#f28a44"/><path d="M2.6 5.2l1.6 1.5 3.2-3.3" stroke="#fff" stroke-width="1.3" fill="none"/></svg>Happy to recommend potential customers</li>
      </ul>
    </div>

    <div class="abs cta" style="left:359px;top:857px">WE'D LOVE TO HEAR FROM YOU, SO PLEASE<br>CONTACT US BY TELEPHONE, TEXT, OR EMAIL:</div>
    <div class="abs phone" style="left:359px;top:902px">
      <svg width="20" height="20" viewBox="0 0 24 24"><path d="M6.6 10.8a15 15 0 006.6 6.6l2.2-2.2c.3-.3.7-.4 1-.2 1.1.4 2.3.6 3.6.6.6 0 1 .4 1 1V20c0 .6-.4 1-1 1A17 17 0 013 4c0-.6.4-1 1-1h3.5c.6 0 1 .4 1 1 0 1.3.2 2.5.6 3.6.1.3 0 .7-.2 1z" fill="none" stroke="#222" stroke-width="1.6"/></svg>0400 555 018
    </div>
    <div class="abs email" style="left:359px;top:930px">hello@neststagingco.com.au</div>
    <div class="abs cta" style="left:359px;top:954px">PLEASE ALSO VISIT OUR WEBSITE</div>
    <div class="abs" style="left:359px;top:975px;font-size:17px;color:var(--ink);font-weight:500">Neststagingco.com.au</div>

    <div class="abs heading" style="left:41px;top:866px">We Reward Referrals!</div>
    <div class="abs voucher-1" style="left:43px;top:902px">WE OFFER A</div>
    <div class="abs voucher-2" style="left:43px;top:942px">$200 GIFT VOUCHER</div>
    <div class="abs voucher-3" style="left:43px;top:974px">FOR EVERY SUCCESSFUL REFERRAL TO US!</div>
  </section>

  <!-- Back side -->
  <section class="page page--back">
    <div class="headline">WE AVERAGE OVER 185 PROPERTY STYLING PROJECTS PER YEAR<br><b>WITH A LARGE PROPORTION SELLING IN LESS THAN 30 DAYS!</b></div>

    <div class="plans">
      <div class="plans-head">PLANS &amp; PRICES</div>
      <div class="plans-grid">
        <div class="plan"><h3>1 BEDROOM PROPERTY</h3><div class="incl">FULL STYLING &nbsp;+&nbsp; 6 WEEKS FREE HIRE*</div><div class="price"><b>1,897.00 AUD</b> I <s>2,750.00</s> I <span>SALE</span></div></div>
        <div class="plan"><h3>3 BEDROOM PROPERTY</h3><div class="incl">FULL STYLING &nbsp;+&nbsp; 6 WEEKS FREE HIRE*</div><div class="price"><b>2,997.00 AUD</b> I <s>4,470.00</s> I <span>SALE</span></div></div>
        <div class="plan"><h3>2 BEDROOM PROPERTY</h3><div class="incl">FULL STYLING &nbsp;+&nbsp; 6 WEEKS FREE HIRE*</div><div class="price"><b>2,697.00 AUD</b> I <s>3,250.00</s> I <span>SALE</span></div></div>
        <div class="plan"><h3>4 BEDROOM PROPERTY</h3><div class="incl">FULL STYLING &nbsp;+&nbsp; 6 WEEKS FREE HIRE*</div><div class="price"><b>3,897.00 AUD</b> I <s>5,485.00</s> I <span>SALE</span></div></div>
      </div>
    </div>
    <div class="footnote"><span>*4 Weeks Free Hire + 2 Weeks Free Extension (if property not sold within 4 weeks)</span></div>

    <div class="photo" style="left:44px;top:377px;width:415px;height:148px">
      <div role="img" aria-label="Open-plan living and kitchen area staged with sofa and dining set" style="background:linear-gradient(180deg,#efefed 0%,#e0dfdb 60%,#cfcac2 100%)"></div>
    </div>
    <div class="photo" style="left:44px;top:539px;width:200px;height:143px">
      <div role="img" aria-label="Covered outdoor living area with lounge and plants" style="background:linear-gradient(180deg,#d9d6d1 0%,#bdb6ad 60%,#8f8a84 100%)"></div>
    </div>
    <div class="photo" style="left:258px;top:539px;width:201px;height:143px">
      <div role="img" aria-label="Stylists dressing a bed with pink throw in a bedroom" style="background:linear-gradient(180deg,#e6e7ea 0%,#d7d2d2 60%,#d6b4b4 100%)"></div>
    </div>
    <div class="photo" style="left:472px;top:377px;width:210px;height:305px">
      <div role="img" aria-label="Stylist arranging patterned cushions on a sofa beside a lamp" style="background:linear-gradient(180deg,#ecebe8 0%,#d3d2d0 55%,#b7b9bf 100%)"></div>
    </div>

    <ul class="benefits">
      <li><svg width="12" height="12" viewBox="0 0 10 10"><circle cx="5" cy="5" r="5" fill="#f28a44"/><path d="M2.6 5.2l1.6 1.5 3.2-3.3" stroke="#fff" stroke-width="1.3" fill="none"/></svg>Helping your property reach its highest potential without busting the budget.</li>
      <li><svg width="12" height="12" viewBox="0 0 10 10"><circle cx="5" cy="5" r="5" fill="#f28a44"/><path d="M2.6 5.2l1.6 1.5 3.2-3.3" stroke="#fff" stroke-width="1.3" fill="none"/></svg>Achieving a record number of viewings &amp; the highest possible sale price.</li>
      <li><svg width="12" height="12" viewBox="0 0 10 10"><circle cx="5" cy="5" r="5" fill="#f28a44"/><path d="M2.6 5.2l1.6 1.5 3.2-3.3" stroke="#fff" stroke-width="1.3" fill="none"/></svg>Installation, interior design &amp; decoration, &amp; removal included.</li>
      <li><svg width="12" height="12" viewBox="0 0 10 10"><circle cx="5" cy="5" r="5" fill="#f28a44"/><path d="M2.6 5.2l1.6 1.5 3.2-3.3" stroke="#fff" stroke-width="1.3" fill="none"/></svg>Pre-sale home preparation to post-sale removal.</li>
      <li><svg width="12" height="12" viewBox="0 0 10 10"><circle cx="5" cy="5" r="5" fill="#f28a44"/><path d="M2.6 5.2l1.6 1.5 3.2-3.3" stroke="#fff" stroke-width="1.3" fill="none"/></svg>Free consultation &amp; longer rental periods.</li>
      <li><svg width="12" height="12" viewBox="0 0 10 10"><circle cx="5" cy="5" r="5" fill="#f28a44"/><path d="M2.6 5.2l1.6 1.5 3.2-3.3" stroke="#fff" stroke-width="1.3" fill="none"/></svg>A small investment for such a large transformation!</li>
    </ul>

    <div class="abs" style="left:470px;top:800px;display:flex;align-items:center;gap:8px"><span class="dot"></span><span class="brand-name" style="font-size:22px">Nest Staging Co</span></div>

    <div class="abs cta" style="left:39px;top:872px;font-size:19px">PLEASE CONTACT US ON</div>
    <div class="abs phone" style="left:39px;top:896px;font-size:32px">
      <svg width="24" height="24" viewBox="0 0 24 24"><path d="M6.6 10.8a15 15 0 006.6 6.6l2.2-2.2c.3-.3.7-.4 1-.2 1.1.4 2.3.6 3.6.6.6 0 1 .4 1 1V20c0 .6-.4 1-1 1A17 17 0 013 4c0-.6.4-1 1-1h3.5c.6 0 1 .4 1 1 0 1.3.2 2.5.6 3.6.1.3 0 .7-.2 1z" fill="none" stroke="#222" stroke-width="1.6"/></svg>0400 555 018
    </div>
    <div class="abs email" style="left:39px;top:929px;font-size:12px">HELLO@NESTSTAGINGCO.COM.AU</div>

    <div class="footer">
      <div>www.<b>Neststagingco</b>.com.au</div>
      <div class="social"><i></i><i></i><i></i></div>
    </div>
  </section>

</div>
</body>
</html>
```